Website design for KORVEL – data platform for healthcare & social housing

We’re looking for a clean, modern multi-page website design for KORVEL — a data platform for healthcare and social housing.

📎 Please read the attached PDF for full structure, context, and design guidance.
The briefing is essential to understanding this project.

➡️ For the initial submission, only the homepage design (including header and footer) is required.

This will help us assess design direction and fit.

The full project includes four levels (homepage, general page, product overview, and product detail), which will be completed after selecting the final designer.

Industry/Entity Type

data platform for healthcare & social housing

Number of Pages Required

1 page

Font styles to use
Sans Serif

Requirements
Must have
• Please read the attached PDF
Nice to have
Should not have

```html
<!DOCTYPE html>
<html lang="en">
<head>
<meta charset="utf-8">
<title>KORVEL – Data platform for healthcare and social housing</title>
<link rel="stylesheet" href="https://fonts.googleapis.com/css2?family=Montserrat:wght@600;700;800&family=Open+Sans:wght@400;600;700&family=Orbitron:wght@500;600&display=swap">
<style>
:root{
  --navy:#0d4a8b;
  --navy-dark:#0a3f7a;
  --orange:#f47b0a;
  --teal:#2bb0bb;
  --teal-light:#d8f1f4;
  --grey-bg:#f1f1f1;
  --text:#3a3a3a;
  --white:#fff;
}
*{box-sizing:border-box;margin:0;padding:0}
html,body{width:1200px;height:4438px;overflow:hidden}
body{position:relative;background:var(--white);font-family:"Open Sans",sans-serif;color:var(--text)}
.abs{position:absolute}
.btn{position:absolute;display:flex;align-items:center;justify-content:center;font-family:"Open Sans",sans-serif;font-size:12.5px;border-radius:3px;color:var(--white);background:var(--navy);text-decoration:none}
.btn-pill{border-radius:20px;font-weight:600}
.btn-orange{background:var(--orange)}
.tech{font-family:"Orbitron",sans-serif;font-weight:500;letter-spacing:2px;text-transform:uppercase}
.accent{color:var(--orange)}
.dash{position:absolute;height:2px;width:28px;background:var(--orange)}
.para{font-size:12.5px;line-height:23px;color:var(--text)}
.photo{position:absolute;overflow:hidden}

/* header */
.site-header{position:absolute;left:0;top:0;width:1200px;height:84px;background:var(--white)}
.logo{position:absolute;font-family:"Montserrat",sans-serif;font-weight:700;color:var(--navy);letter-spacing:4px}
.main-nav{position:absolute;top:36px;font-size:12.5px;color:#333}
.main-nav span{position:absolute;white-space:nowrap}

/* hero */
.hero{position:absolute;left:0;top:84px;width:1200px;height:531px;background:linear-gradient(90deg,#f4f8fd 0%,#e9f0fa 38%,#c4d8f2 62%,#7aa6de 100%)}
.hero-title{position:absolute;left:138px;top:128px;font-family:"Montserrat",sans-serif;font-weight:800;font-size:40px;line-height:54px;color:var(--navy)}
.hero-sub{position:absolute;left:138px;top:316px;font-size:13.5px;font-weight:600;color:#111}

/* framed photos */
.frame{position:absolute;border:5px solid var(--teal);border-top:none;border-left:none;border-radius:0 0 22px 0}

/* helps */
.help-col{position:absolute;width:220px;text-align:center}
.help-icon{width:72px;height:72px;border-radius:50%;background:var(--teal-light);margin:0 auto;display:flex;align-items:center;justify-content:center}
.help-title{margin-top:24px;font-size:15px;font-weight:600;color:var(--navy)}
.help-text{margin-top:14px;font-size:12.5px;line-height:20px}

/* products */
.product-card{position:absolute;top:1882px;width:211px;height:280px;background:var(--white);border-radius:10px;box-shadow:0 4px 14px rgba(0,0,0,.06);padding:38px 16px 0}
.product-card .ico{width:70px;height:70px;border-radius:50%;background:var(--teal-light);display:flex;align-items:center;justify-content:center}
.product-card h3{margin-top:24px;font-size:14.5px;font-weight:600;color:var(--navy)}
.product-card .rule{width:28px;height:2px;background:var(--orange);margin-top:10px}
.product-card p{margin-top:12px;font-size:12px;line-height:20px}
.product-card .arrow{margin-top:10px}
.product-card.active{background:var(--navy);color:var(--white)}
.product-card.active h3{color:var(--white)}
.product-card.active .ico{background:var(--teal)}

/* testimonials */
.review{position:absolute;top:3354px;width:268px;height:232px;background:var(--white);border-radius:8px;box-shadow:0 3px 14px rgba(0,0,0,.09);padding:22px 20px}
.review .stars{color:var(--orange);font-size:14px;letter-spacing:2px}
.review p{margin-top:12px;font-size:12.5px;line-height:21px}
.review .person{position:absolute;left:20px;top:172px;display:flex;align-items:center;gap:10px}
.review .avatar{width:44px;height:44px;border-radius:50%;border:2px solid #eee;background:radial-gradient(circle at 50% 40%,#e3cdb7 0%,#b89479 45%,#5d4d44 100%)}
.review .name{font-size:12.5px;color:var(--navy)}
.review .role{font-size:11px}
.quote{position:absolute;width:52px;height:52px;border-radius:50%;background:var(--teal);color:var(--white);font-family:"Montserrat",sans-serif;font-size:48px;font-weight:800;line-height:68px;text-align:center}

/* footer */
.site-footer{position:absolute;left:0;top:3860px;width:1200px;height:522px;background:var(--navy)}
.footer-head{position:absolute;font-size:14px;font-weight:600;color:var(--white);letter-spacing:.5px}
.footer-links{position:absolute;font-size:12.5px;line-height:23px;color:var(--white)}
.contact-row{position:absolute;display:flex;gap:10px;font-size:12.5px;line-height:19px;color:var(--white)}
.social-row{position:absolute;display:flex;align-items:center;gap:10px;font-size:12.5px;color:var(--white)}
.social-row i{width:28px;height:28px;border:1.5px solid var(--white);border-radius:50%;display:block}
.bottom-bar{position:absolute;left:0;top:4382px;width:1200px;height:56px;background:var(--teal);color:var(--white);font-size:12.5px}
</style>
</head>
<body>

<!-- Header -->
<header class="site-header">
  <div class="logo" style="left:60px;top:26px;font-size:26px">KORVEL</div>
  <nav class="main-nav">
    <span style="left:257px">What is KORVEL?</span>
    <span style="left:380px">Products</span>
    <span style="left:465px">Who it's for</span>
    <span style="left:565px">Community</span>
    <span style="left:668px">About us</span>
    <span style="left:754px">Contact</span>
  </nav>
  <a class="btn btn-pill" style="left:850px;top:27px;width:136px;height:36px;background:var(--white);color:var(--navy);border:1.5px solid var(--navy)">Plan a Demo</a>
  <a class="btn btn-pill btn-orange" style="left:1002px;top:27px;width:134px;height:36px">Start KORVEL</a>
</header>

<!-- Hero -->
<section class="hero">
  <div class="photo" role="img" aria-label="Blue medical data visual with a stethoscope, hexagons, a digital world map and health graphics" style="left:520px;top:0;width:680px;height:531px;background:radial-gradient(ellipse at 70% 55%,#eaf2fd 0%,#a9c6ee 28%,rgba(120,162,222,.6) 55%,rgba(220,232,248,0) 80%),linear-gradient(100deg,rgba(230,238,250,0) 0%,#9dbde8 50%,#3f78c8 100%)"></div>
  <h1 class="hero-title">More Impact With<br>Better Control Over<br>Data</h1>
  <p class="hero-sub">Data Analytics For Healthcare And Social Housing</p>
  <a class="btn btn-pill btn-orange" style="left:138px;top:367px;width:133px;height:36px">Products</a>
  <a class="btn btn-pill" style="left:286px;top:367px;width:155px;height:36px">Plan a Demo</a>
</section>

<!-- About -->
<section>
  <div class="frame" style="left:150px;top:727px;width:420px;height:385px"></div>
  <div class="photo" role="img" aria-label="Woman in a dark blazer working on a laptop showing a spreadsheet" style="left:138px;top:715px;width:425px;height:387px;border-radius:18px;background:radial-gradient(ellipse at 35% 40%,#c9b09a 0%,rgba(120,100,90,0) 35%),radial-gradient(ellipse at 72% 55%,#dfe8ec 0%,rgba(200,210,215,0) 30%),linear-gradient(135deg,#e2ddd4 0%,#9b9690 45%,#3e4248 100%)"></div>
  <div class="dash" style="left:637px;top:762px;height:1.5px"></div>
  <div class="abs accent" style="left:673px;top:755px;font-size:11.5px">ABOUT US</div>
  <h2 class="abs tech" style="left:637px;top:776px;font-size:27px;color:var(--navy)">KORVEL <span class="accent">DATA CLARITY</span></h2>
  <p class="abs para" style="left:637px;top:818px;width:420px">KORVEL is a data analytics platform for the healthcare sector and social housing sector. It helps organizations unlock, analyze, and use data to make smarter decisions. KORVEL combines a scalable platform with intelligent tools, a professional community, and BI-as-a-Service. Lorem ipsum dolor sit amet, consectetuer adipiscing elit, sed diam fhd nonum my nibh euismod tincidunt ut laoreet dolore magna aliquam erat volutpat. Ut wisi enim ad minim veniam, quis nostrud exerci quat. tation ullamcorper suscipit lobortis nisl ut aliquip ex ea commodo con.</p>
  <a class="btn" style="left:637px;top:1028px;width:127px;height:34px">What is KORVEL?</a>
</section>

<!-- How it helps -->
<section>
  <div class="abs" aria-hidden="true" style="left:0;top:1196px;width:1200px;text-align:center;font-family:'Orbitron',sans-serif;font-weight:600;font-size:120px;letter-spacing:24px;color:#e1e8f1">KORVEL</div>
  <h2 class="abs tech" style="left:0;top:1304px;width:1200px;text-align:center;font-size:26px;color:var(--navy)">How KORVEL <span class="accent">Helps</span></h2>
  <div class="help-col" style="left:220px;top:1357px">
    <div class="help-icon"><svg width="40" height="40" viewBox="0 0 40 40" fill="none" stroke="#0d4a8b" stroke-width="1.6"><rect x="5" y="7" width="30" height="20" rx="2"/><path d="M15 33h10M20 27v6"/><circle cx="20" cy="17" r="4" stroke="#f47b0a"/><path d="M20 10v2M20 22v2M13 17h2M25 17h2M15 12l1.5 1.5M23.5 20.5L25 22M25 12l-1.5 1.5M16.5 20.5L15 22" stroke="#f47b0a"/></svg></div>
    <div class="help-title">Platform and Products</div><p class="help-text">Lorem ipsum dolor sit amet, consectetuer adipiscing elit, sed diam nonum my nibh euismod.</p></div>
  <div class="help-col" style="left:487px;top:1357px">
    <div class="help-icon"><svg width="40" height="40" viewBox="0 0 40 40" fill="none" stroke="#0d4a8b" stroke-width="1.6"><circle cx="20" cy="20" r="4" stroke="#f47b0a"/><circle cx="8" cy="9" r="3"/><circle cx="32" cy="9" r="3"/><circle cx="8" cy="31" r="3"/><circle cx="32" cy="31" r="3"/><circle cx="20" cy="5" r="2.5"/><circle cx="20" cy="35" r="2.5"/><path d="M10 11l7 6M30 11l-7 6M10 29l7-6M30 29l-7-6M20 8v8M20 24v8"/></svg></div>
    <div class="help-title">Community</div><p class="help-text">Lorem ipsum dolor sit amet, consectetuer adipiscing elit, sed diam nonum my nibh euismod.</p></div>
  <div class="help-col" style="left:756px;top:1357px">
    <div class="help-icon"><svg width="40" height="40" viewBox="0 0 40 40" fill="none" stroke="#0d4a8b" stroke-width="1.6"><rect x="12" y="5" width="22" height="28" rx="2"/><path d="M17 12h12M17 17h8"/><path d="M17 28v-4M22 28v-7M27 28v-5" stroke="#f47b0a" stroke-width="2"/><path d="M5 14h5M5 20h5M5 26h5"/><circle cx="5" cy="14" r="1"/><circle cx="5" cy="20" r="1"/><circle cx="5" cy="26" r="1"/></svg></div>
    <div class="help-title">BI-as-a-Service</div><p class="help-text">Lorem ipsum dolor sit amet, consectetuer adipiscing elit, sed diam nonum my nibh euismod.</p></div>
  <a class="btn" style="left:542px;top:1577px;width:113px;height:34px">More Info</a>
</section>

<!-- Products overview -->
<section>
  <div class="abs" style="left:0;top:1716px;width:1200px;height:832px;background:var(--grey-bg)"></div>
  <div class="dash" style="left:586px;top:1815px"></div>
  <h2 class="abs tech" style="left:0;top:1824px;width:1200px;text-align:center;font-size:26px;color:var(--navy)">Products Overview</h2>
  <article class="product-card" style="left:139px">
    <div class="ico"><svg width="40" height="40" viewBox="0 0 40 40" fill="none" stroke="#0d4a8b" stroke-width="1.6"><path d="M6 20c0-7 6-12 14-12s14 5 14 12"/><rect x="10" y="16" width="20" height="8" rx="2"/><circle cx="14" cy="20" r="1.5"/><circle cx="26" cy="20" r="1.5"/><path d="M9 34V27h5v7M17 34v-5h5v5M25 34v-7h5v7" stroke="#f47b0a"/></svg></div>
    <h3>Public Data Access</h3><div class="rule"></div><p>Lorem ipsum dolor sit amet, consectetuer adipiscing elit, it sed diam nonum my nibh eui.</p><svg class="arrow" width="22" height="14" viewBox="0 0 22 14"><path d="M1 7h18M13 1l6 6-6 6" stroke="#f47b0a" stroke-width="2.4" fill="none"/></svg></article>
  <article class="product-card" style="left:375px">
    <div class="ico"><svg width="40" height="40" viewBox="0 0 40 40" fill="none" stroke="#0d4a8b" stroke-width="1.6"><rect x="10" y="5" width="20" height="30" rx="2"/><path d="M14 11h12M14 16h12M14 21h8"/><path d="M5 26h30" stroke="#f47b0a" stroke-width="2"/><path d="M14 30h12"/></svg></div>
    <h3>Climate Risk Scan</h3><div class="rule"></div><p>Lorem ipsum dolor sit amet, consectetuer adipiscing elit, it sed diam nonum my nibh eui.</p><svg class="arrow" width="22" height="14" viewBox="0 0 22 14"><path d="M1 7h18M13 1l6 6-6 6" stroke="#f47b0a" stroke-width="2.4" fill="none"/></svg></article>
  <article class="product-card active" style="left:611px">
    <div class="ico"><svg width="40" height="40" viewBox="0 0 40 40" fill="none" stroke="#fff" stroke-width="1.7"><path d="M6 34h22"/><path d="M9 34V24M14 34V20M19 34V26M24 34V22"/><circle cx="27" cy="13" r="7"/><path d="M27 9v4l3 2"/></svg></div>
    <h3>Pricing Benchmark</h3><div class="rule"></div><p>Lorem ipsum dolor sit amet, consectetuer adipiscing elit, it sed diam nonum my nibh eui.</p><svg class="arrow" width="22" height="14" viewBox="0 0 22 14"><path d="M1 7h18M13 1l6 6-6 6" stroke="#2bb0bb" stroke-width="2.4" fill="none"/></svg></article>
  <article class="product-card" style="left:847px">
    <div class="ico"><svg width="40" height="40" viewBox="0 0 40 40" fill="none" stroke="#0d4a8b" stroke-width="1.6"><circle cx="24" cy="15" r="9"/><circle cx="24" cy="15" r="4" stroke="#f47b0a"/><ellipse cx="12" cy="30" rx="7" ry="2.5" stroke="#f47b0a"/><path d="M5 30v3c0 1.4 3 2.5 7 2.5s7-1.1 7-2.5v-3" stroke="#f47b0a"/><path d="M24 6V3M33 15h3"/></svg></div>
    <h3>Cost Model</h3><div class="rule"></div><p>Lorem ipsum dolor sit amet, consectetuer adipiscing elit, it sed diam nonum my nibh eui.</p><svg class="arrow" width="22" height="14" viewBox="0 0 22 14"><path d="M1 7h18M13 1l6 6-6 6" stroke="#f47b0a" stroke-width="2.4" fill="none"/></svg></article>
  <a class="btn" style="left:528px;top:2214px;width:142px;height:34px">View All Products</a>
</section>

<!-- Who is it for -->
<section>
  <div class="abs" style="left:138px;top:2342px;width:499px;height:389px;background:var(--orange);border-radius:8px 0 0 8px"></div>
  <div class="photo" role="img" aria-label="Smiling sales manager in a blue suit shaking hands across a desk" style="left:637px;top:2342px;width:422px;height:389px;border-radius:0 8px 8px 0;background:radial-gradient(ellipse at 45% 55%,#3f5f96 0%,rgba(40,60,100,0) 40%),radial-gradient(ellipse at 42% 28%,#c89878 0%,rgba(150,110,80,0) 18%),linear-gradient(135deg,#7a5234 0%,#4a3a32 45%,#1d2230 100%)"></div>
  <div class="abs" style="left:637px;top:2699px;width:422px;text-align:center;font-family:'Orbitron',sans-serif;font-size:26px;letter-spacing:2px;color:rgba(255,255,255,.45)">SALES MANAGERS</div>
  <div class="abs" style="left:188px;top:2406px;width:28px;height:2px;background:var(--white)"></div>
  <h2 class="abs tech" style="left:188px;top:2414px;font-size:26px;color:var(--white)">Who is KORVEL for?</h2>
  <div class="abs" style="left:188px;top:2469px;font-size:16px;font-weight:600;color:#111">Sales Managers</div>
  <p class="abs para" style="left:188px;top:2495px;width:410px;color:var(--white)">Lorem ipsum dolor sit amet, consectetuer adipiscing elit, sed diam nonummy nibh euismod tincidunt ut laoreet dolore magna aliquam erat volutpat. Ut wisi enim ad minim veniam, quis nostrud exerci tation ullamcorper suscipit lobortis nisl ut aliquip ex ea commodo consequat. Duis autem vel eum iriure dolor in hendrerit in vulputat.</p>
  <a class="btn" style="left:188px;top:2632px;width:127px;height:35px">Who is it For?</a>
  <svg class="abs" style="left:512px;top:2632px" width="80" height="36" viewBox="0 0 80 36">
    <circle cx="18" cy="18" r="17" fill="#fff"/><path d="M26 18H10M16 12l-6 6 6 6" stroke="#f47b0a" stroke-width="2.2" fill="none"/>
    <circle cx="60" cy="18" r="17" fill="#0d4a8b" stroke="#fff" stroke-width="1.5"/><path d="M52 18h16M62 12l6 6-6 6" stroke="#fff" stroke-width="2.2" fill="none"/>
  </svg>
</section>

<!-- Community -->
<section>
  <div class="frame" style="left:176px;top:2850px;width:390px;height:320px"></div>
  <div class="photo" role="img" aria-label="Team members stacking their hands together over a table" style="left:138px;top:2837px;width:425px;height:321px;border-radius:18px;background:radial-gradient(ellipse at 55% 50%,#d6a98c 0%,#b7876c 25%,rgba(150,120,110,0) 55%),linear-gradient(135deg,#e4e7ea 0%,#9aa3ad 50%,#46505d 100%)"></div>
  <div class="dash" style="left:637px;top:2842px"></div>
  <h2 class="abs tech" style="left:637px;top:2847px;font-size:27px;color:var(--navy)">Our <span class="accent">Community</span></h2>
  <p class="abs para" style="left:637px;top:2890px;width:420px">Lorem ipsum dolor sit amet, consectetuer adipiscing elit, sed diam nonum my nibh euismod tincidunt ut laoreet dolore magna aliquam erat volutpat. Ut wisi enim ad minim veniam, quis nostrud exercisdg.y tation ullamcorper suscipit lobortis nisl ut aliquip ex ea commodo dfp.</p>
  <p class="abs para" style="left:637px;top:2988px;width:420px">Duis autem vello eum iriure dolor in hendrerit in vulputate velit esse molestie consequat, vel illum dolore eu feugiat nulla facilisis at vero eros et accumsan et iusto odio dignissim qui blandit praesentuis autem vello eum iriure dolor in hendrerit in vulputate velit esse molestie consequat, vel illum dolore eu feugiat nulla facilisis at.</p>
  <a class="btn" style="left:637px;top:3128px;width:157px;height:34px">Join The Community</a>
</section>

<!-- Testimonials -->
<section>
  <div class="dash" style="left:586px;top:3271px"></div>
  <h2 class="abs tech" style="left:0;top:3282px;width:1200px;text-align:center;font-size:26px;color:var(--navy)">Satisfied Client <span class="accent">or Partner</span></h2>
  <article class="review" style="left:139px"><div class="stars">★★★★★</div><p>Lorem ipsum dolor sit amet, consectetuer adipiscing elit, sed diam nonum my nibh euismod tincidunt ut laoreet dolore magna aliquam erat volutpat. Ut wisi enim ad minim</p><div class="person"><div class="avatar" role="img" aria-label="Client portrait"></div><div><div class="name">Mark Delaney</div><div class="role">Lorem ipsum</div></div></div></article>
  <article class="review" style="left:456px"><div class="stars">★★★★★</div><p>Lorem ipsum dolor sit amet, consectetuer adipiscing elit, sed diam nonum my nibh euismod tincidunt ut laoreet dolore magna aliquam erat volutpat. Ut wisi enim ad minim</p><div class="person"><div class="avatar" role="img" aria-label="Partner portrait"></div><div><div class="name">Nina Foster</div><div class="role">Lorem ipsum</div></div></div></article>
  <article class="review" style="left:771px"><div class="stars">★★★★★</div><p>Lorem ipsum dolor sit amet, consectetuer adipiscing elit, sed diam nonum my nibh euismod tincidunt ut laoreet dolore magna aliquam erat volutpat. Ut wisi enim ad minim</p><div class="person"><div class="avatar" role="img" aria-label="Client portrait"></div><div><div class="name">Paul Brennan</div><div class="role">Lorem ipsum</div></div></div></article>
  <div class="quote" style="left:373px;top:3335px">“</div>
  <div class="quote" style="left:689px;top:3335px">“</div>
  <div class="quote" style="left:1005px;top:3335px">“</div>
  <svg class="abs" style="left:555px;top:3614px" width="86" height="20" viewBox="0 0 86 20">
    <circle cx="10" cy="10" r="7" fill="#8fd3da"/><circle cx="32" cy="10" r="7" fill="#0d4a8b" stroke="#8fd3da" stroke-width="3"/><circle cx="54" cy="10" r="7" fill="#8fd3da"/><circle cx="75" cy="10" r="7" fill="#8fd3da"/>
  </svg>
</section>

<!-- Footer -->
<footer class="site-footer">
  <div class="logo" style="left:138px;top:210px;font-size:34px;color:var(--white);letter-spacing:6px">KORVEL</div>
  <p class="abs" style="left:138px;top:276px;width:260px;font-size:12.5px;line-height:20px;color:var(--white)">Lorem ipsum dolor sit amet, consectetuer adipiscing elit, sed diam nonum my nibh euismod tincidunt ut laoreet dolore magna aliquam erat volutpat. Ut wisi enim ad minim veniam, quis nostrud exerci tation ullamcorper suscipit lobortis nisl ut aliqui.</p>

  <div class="abs" style="left:487px;top:226px;width:28px;height:2px;background:var(--orange)"></div>
  <div class="footer-head" style="left:487px;top:238px">QUICK LINKS</div>
  <div class="footer-links" style="left:487px;top:262px">What is KORVEL?<br>Products<br>Who It's For<br>Community<br>About Us<br>Contact</div>

  <div class="abs" style="left:670px;top:226px;width:28px;height:2px;background:var(--orange)"></div>
  <div class="footer-head" style="left:670px;top:238px">CONTACT DETAILS</div>
  <div class="contact-row" style="left:670px;top:267px"><svg width="28" height="30" viewBox="0 0 28 30"><path d="M14 27s-9-9-9-15a9 9 0 0 1 18 0c0 6-9 15-9 15z" stroke="#fff" stroke-width="1.6" fill="none"/><circle cx="14" cy="12" r="3" stroke="#fff" stroke-width="1.6" fill="none"/></svg><div>123, Building Name, Street<br>City, State XY 123456</div></div>
  <div class="contact-row" style="left:670px;top:313px"><svg width="28" height="30" viewBox="0 0 28 30"><path d="M7 4l5 1 2 6-3 2a14 14 0 0 0 6 6l2-3 6 2 1 5c-1 2-3 3-5 3C11 26 2 17 3 7c0-2 2-3 4-3z" stroke="#fff" stroke-width="1.6" fill="none"/></svg><div>PHONE<br>+001 123 456 7890</div></div>
  <div class="contact-row" style="left:670px;top:360px"><svg width="28" height="30" viewBox="0 0 28 30"><rect x="3" y="7" width="22" height="16" rx="2" stroke="#fff" stroke-width="1.6" fill="none"/><path d="M3 9l11 8 11-8" stroke="#fff" stroke-width="1.6" fill="none"/></svg><div>EMAIL<br>info@korveldata.com</div></div>

  <div class="abs" style="left:961px;top:226px;width:28px;height:2px;background:var(--orange)"></div>
  <div class="footer-head" style="left:961px;top:238px">FOLLOW US</div>
  <div class="social-row" style="left:961px;top:266px"><i></i>Netlink</div>
  <div class="social-row" style="left:961px;top:298px"><i></i>Postwire</div>
  <div class="social-row" style="left:961px;top:330px"><i></i>Friendhub</div>
  <div class="social-row" style="left:961px;top:362px"><i></i>Pixfeed</div>

  <div class="abs" style="left:138px;top:427px;width:921px;height:1px;background:rgba(255,255,255,.3)"></div>
  <p class="abs" style="left:138px;top:454px;width:921px;font-size:11.5px;line-height:17px;color:var(--white)"><b>Disclaimer:</b> Lorem ipsum dolor sit amet, consectetuer adipiscing elit, sed diam nonum my nibh euismod tincidunt ut laoreet dolore magna aliquam erat volutpat. Ut wisi enim ad minim veniam, quis nostrud exerci tation ullamcorper suscipit lobortis nisl ut aliquip ex ea commodo consequat.Duis autem vello eum iriure dolor in hendrerit in.</p>
</footer>

<!-- Call to action -->
<section class="abs" style="left:246px;top:3740px;width:706px;height:246px;background:var(--teal);border-radius:22px;text-align:center;color:var(--white)">
  <h2 style="margin-top:42px;font-family:'Montserrat',sans-serif;font-weight:800;font-size:31px;line-height:43px">MORE IMPACT WITH<br>BETTER CONTROL OVER DATA</h2>
  <p style="margin-top:6px;font-size:14px">Data analytics for healthcare and social housing</p>
  <a class="btn" style="left:229px;top:167px;width:106px;height:34px">Start KORVEL</a>
  <a class="btn btn-orange" style="left:348px;top:167px;width:102px;height:34px">Plan A Demo</a>
</section>

<div class="bottom-bar">
  <span class="abs" style="left:138px;top:19px">© 2025 KORVEL. All Rights Reserved.</span>
  <span class="abs" style="left:816px;top:19px">Privacy Policy &nbsp; | &nbsp; Terms and conditions</span>
</div>

</body>
</html>
```